Main pic needed for new travel site's homepage

New travel site needs a main pic to showcase on their homepage. The pic should include the text 'Travel Smarter', but this text COULD change so we need to take that into account. The showcase pic you will be designing will replace the current beach pic seen at www.lagunokvisto.net.
The art should be FUN, CONTEMPORARY, BOLD, TRENDY, but not overly busy.
Updates

We are NOT looking for a stock photo that I can go get myself.  I am very familiar with stock photos.  We are looking for a bold design that CAN include a stock photo.  In such cases, the stock photo will most likely need to be touched up to work well with this theme. 

Industry/Entity Type

Travel

Requirements
Must have
• We are likely to keep the current color scheme seen on the homepage so the pic will need to compliment these colors.
Should not have
• The main part of the showcase graphic should not be on the left as the 'Plan your next vacation' box is staying on top. The design is simply being swapped out with the beach scene. The 'Plan your next vacation' box that hovers over the showcase pic is staying put.

```html
<!DOCTYPE html>
<html lang="en">
<head>
<meta charset="utf-8">
<title>LagunokVisto – Plan your next vacation</title>
<link rel="stylesheet" href="https://fonts.googleapis.com/css2?family=Open+Sans:wght@400;600;700&family=Montserrat:wght@100;200;800;900&display=swap">
<style>
:root{
  --purple:#7e2470;
  --purple-dark:#6c1c60;
  --teal:#2c8c86;
  --text:#333;
  --muted:#666;
  --card-bg:#efefef;
  --line:#d6d6d6;
  --white:#fff;
  --sky-deep:#1f5fb8;
  --sky:#4f9ee0;
  --sea:#3fc0d6;
  --sea-light:#a6e6ea;
  --sand:#eadbc8;
  --sand-warm:#dcc5a6;
  --wood:#b8742e;
}
*{box-sizing:border-box;margin:0;padding:0}
html,body{width:1200px;height:614px;overflow:hidden;background:var(--white);font-family:"Open Sans",Arial,sans-serif;color:var(--text)}
.page{position:relative;width:1200px;height:614px;overflow:hidden}

.site-header{height:50px;position:relative}
.brand{position:absolute;left:70px;top:8px;display:flex;align-items:center;gap:8px}
.brand-dot{width:30px;height:30px;border-radius:50%;background:var(--purple)}
.brand-name{font-size:24px;font-weight:600;color:var(--teal);letter-spacing:-.3px}
.contact{position:absolute;right:80px;top:9px;text-align:right;line-height:1}
.contact-label{font-size:10px;color:var(--muted)}
.contact-phone{font-size:19px;color:#555;margin-top:2px}

.main-nav{height:29px;background:var(--purple);display:flex;align-items:center;padding:0 66px;font-size:11px;color:var(--white)}
.main-nav a{color:var(--white);text-decoration:none;margin-right:21px}
.main-nav a.current{color:#d6b9d1}
.main-nav .account{margin-left:auto;display:flex}
.main-nav .account a{margin:0 0 0 21px}

.hero{position:relative;height:330px;overflow:hidden}
.hero-photo{position:absolute;inset:0;background:
  radial-gradient(ellipse 190px 150px at 1110px 330px,rgba(184,116,46,.85),rgba(184,116,46,0) 75%),
  radial-gradient(ellipse 70px 110px at 1030px 250px,rgba(240,120,80,.55),rgba(240,120,80,0) 80%),
  radial-gradient(ellipse 320px 140px at 120px 0,rgba(10,40,100,.55),rgba(10,40,100,0) 80%),
  radial-gradient(ellipse 260px 120px at 1200px 0,rgba(20,60,120,.5),rgba(20,60,120,0) 80%),
  radial-gradient(ellipse 300px 60px at 690px 290px,rgba(200,170,130,.45),rgba(200,170,130,0) 80%),
  linear-gradient(180deg,var(--sky-deep) 0%,var(--sky) 30%,#8cc8ec 50%,var(--sea) 55%,var(--sea-light) 62%,var(--sand) 68%,#f1e6d7 82%,var(--sand-warm) 100%)}
.hero-title{position:absolute;left:518px;top:18px;line-height:1;pointer-events:none}
.hero-title .light{display:block;font-family:"Montserrat",sans-serif;font-weight:100;font-size:96px;color:var(--purple);letter-spacing:-5px}
.hero-title .bold{display:block;font-family:"Montserrat",sans-serif;font-weight:900;font-size:124px;color:var(--white);letter-spacing:-6px;margin-top:-34px;text-shadow:0 2px 6px rgba(0,0,0,.15)}

.search-box{position:absolute;left:68px;top:33px;width:430px;height:262px;background:var(--white);border-radius:3px;box-shadow:0 2px 6px rgba(0,0,0,.35);padding:16px 20px}
.search-box h1{font-size:20px;font-weight:600;color:#333}
.search-box h2{font-size:13.5px;font-weight:600;margin-top:4px}
.radio{display:inline-flex;align-items:center;gap:6px;font-size:11px;color:#555}
.radio i{width:11px;height:11px;border:1px solid #888;border-radius:50%;display:inline-block;position:relative}
.radio i.on::after{content:"";position:absolute;inset:2px;border-radius:50%;background:#333}
.dest-row{display:flex;align-items:center;gap:5px;margin-top:6px}
.dest-input{width:250px;height:19px;border:1px solid #ccc;border-radius:2px;font-size:10.5px;color:#aaa;padding:2px 6px}
.places{display:grid;grid-template-columns:100px 100px 100px 100px;row-gap:5px;margin-top:5px}
.divider{border-top:1px solid var(--line);margin:10px 0 10px}
.fields{display:grid;grid-template-columns:103px 97px 100px 90px;font-size:14px;font-weight:600}
.field-ctrl{margin-top:6px;height:24px;border:1px solid #ccc;border-radius:2px;font-size:11px;font-weight:400;color:#aaa;display:flex;align-items:center;padding-left:5px;position:relative}
.select{width:72px}
.select::after{content:"▾";position:absolute;right:0;top:0;width:17px;height:22px;border-left:1px solid #ccc;background:#eee;color:#888;font-size:10px;display:flex;align-items:center;justify-content:center}
.select .x{position:absolute;right:24px;color:#777;font-size:11px}
.search-btn{position:absolute;right:20px;top:215px;background:var(--purple);color:var(--white);font-size:12.5px;padding:5px 10px;border-radius:2px;border:1px solid var(--purple-dark);display:flex;align-items:center;gap:4px}

.featured{position:absolute;left:66px;top:416px;width:1045px;height:210px;border:1px solid var(--line)}
.featured-head{height:45px;background:linear-gradient(#f6f6f6,#e4e4e4);border-bottom:1px solid var(--line);padding:8px 10px}
.featured-head h2{font-size:24px;font-weight:600;color:#333}
.card{position:absolute;width:321px;height:111px;background:var(--card-bg);border:1px solid var(--line);padding:9px}
.card .thumb{float:left;width:114px;height:85px;border:4px solid var(--white);box-shadow:0 0 2px rgba(0,0,0,.2);margin-right:10px}
.thumb.maui{background:radial-gradient(ellipse 40px 20px at 30px 18px,#c2d8b0,rgba(194,216,176,0)),linear-gradient(180deg,#dfe8ef 0%,#8cb26a 30%,#a35a3a 48%,#6f4a2e 58%,#5f9a3c 70%,#3f7a2a 100%)}
.thumb.daytona{background:radial-gradient(ellipse 24px 34px at 52px 38px,#e8ecef,rgba(232,236,239,0) 90%),linear-gradient(180deg,#3f8ad0 0%,#7fb8e6 40%,#cfd9e0 62%,#3fb6d0 80%,#7ccde0 100%)}
.thumb.clermont{background:radial-gradient(ellipse 30px 18px at 55px 42px,#f3d8d8,rgba(243,216,216,0)),linear-gradient(180deg,#2f6fc0 0%,#6aa3de 45%,#b8c8b0 60%,#4d8a3a 78%,#3a6e2a 100%)}
.card h3{font-size:12px;font-weight:700;color:var(--purple);margin-top:5px}
.card .loc{font-size:11px;font-weight:700;color:#333}
.card p{font-size:9.5px;color:#666;line-height:1.25;margin-top:3px}
.card.next{height:40px}
</style>
</head>
<body>
<div class="page">
  <header class="site-header">
    <div class="brand"><span class="brand-dot"></span><span class="brand-name">LagunokVisto</span></div>
    <div class="contact"><div class="contact-label">Questions? Call Us.</div><div class="contact-phone">888.555.0142</div></div>
  </header>

  <nav class="main-nav">
    <a class="current">Home</a><a>Resorts</a><a>Flights</a><a>Cruises</a><a>Cars</a><a>Deals</a>
    <div class="account"><a>Login</a><a>Register</a></div>
  </nav>

  <section class="hero">
    <div class="hero-photo" role="img" aria-label="Beach scene with palm trees, a hammock on white sand and a tropical cocktail on a wooden table by the sea"></div>
    <div class="hero-title"><span class="light">Travel</span><span class="bold">Smarter</span></div>

    <form class="search-box">
      <h1>Plan your next vacation</h1>
      <h2>Where would you like to go?</h2>
      <div class="dest-row"><span class="radio"><i class="on"></i>Desired Destination:</span><span class="dest-input">city, state, resort name...</span></div>
      <div class="places">
        <span class="radio"><i></i>Orlando</span><span class="radio"><i></i>Hawaii</span><span class="radio"><i></i>Cancún</span><span class="radio"><i></i>Gatlinburg</span>
        <span class="radio"><i></i>Daytona</span><span class="radio"><i></i>Las Vegas</span><span class="radio"><i></i>Hilton Head</span><span class="radio"><i></i>Atlantic City</span>
      </div>
      <div class="divider"></div>
      <div class="fields">
        <div>Check in &nbsp;-or-<div class="field-ctrl" style="width:83px">mm/dd/yyyy</div></div>
        <div>Week #<div class="field-ctrl select"><span class="x">×</span></div></div>
        <div>Bedrooms<div class="field-ctrl select"><span class="x">×</span></div></div>
        <div>Buy or rent<div class="field-ctrl select" style="color:#888">Buy</div></div>
      </div>
      <div class="search-btn">Search
        <svg width="12" height="12" viewBox="0 0 12 12"><path d="M1 6h9M6 2l4 4-4 4" stroke="#fff" stroke-width="2" fill="none"/></svg>
      </div>
    </form>
  </section>

  <section class="featured">
    <div class="featured-head"><h2>Featured Resorts</h2></div>
    <article class="card" style="left:13px;top:57px">
      <div class="thumb maui" role="img" aria-label="Resort buildings among tropical trees and lawn"></div>
      <h3>Palm Ridge Falls</h3><div class="loc">Lahaina, Maui, HI</div>
      <p>Week: Floating<br>Size: 1 bed; 2 bath<br>Buy: $0 &nbsp;|&nbsp; Rent: $0</p>
    </article>
    <article class="card" style="left:359px;top:57px">
      <div class="thumb daytona" role="img" aria-label="Beachfront hotel tower with a pool"></div>
      <h3>Coral Tide Resort</h3><div class="loc">Daytona Beach, FL</div>
      <p>Week: 6<br>Size: Studio; 1 bath<br>Buy: $0 &nbsp;|&nbsp; Rent: $0</p>
    </article>
    <article class="card" style="left:705px;top:57px">
      <div class="thumb clermont" role="img" aria-label="Resort entrance with palm trees and lawn"></div>
      <h3>Sunset Grove Resort</h3><div class="loc">Clermont, FL</div>
      <p>Week: Points<br>Size: 2 bed; 2 bath<br>Buy: $0 &nbsp;|&nbsp; Rent: $0</p>
    </article>
    <div class="card next" style="left:13px;top:189px"></div>
    <div class="card next" style="left:359px;top:189px"></div>
    <div class="card next" style="left:705px;top:189px"></div>
  </section>
</div>
</body>
</html>
```